Brom-leigh Sky Harbour Custom Brokers Limited

Shop online from the USA and Ship to Jamaica
Customs Brokerage, Import Export and logistic Services
Address:- 238-240 Halden Brook Road Kingston Jamaica
Email: info@bromleighskyharbour,com
Web: www.bromleighskyharbour.com
Telephone: (876) 555-0148, (876) 555-0193
flyer should be quarter page must print information on back and front

```html
<!DOCTYPE html>
<html lang="en">
<head>
<meta charset="UTF-8">
<title>Brom-leigh Sky Harbour Custom Brokers Limited – Flyer Front and Back</title>
<link href="https://fonts.googleapis.com/css2?family=Montserrat:wght@600;700;800;900&family=Open+Sans:wght@400;600;700&display=swap" rel="stylesheet">
<style>
  :root {
    --navy: #13264f;
    --orange: #f39a1c;
    --yellow: #f7c21a;
    --white: #ffffff;
    --text: #3a4257;
    --muted: #6b7388;
    --panel: #f3f5f9;
    --page: #eceef2;
  }
  * { box-sizing: border-box; margin: 0; padding: 0; }
  html, body { width: 837px; height: 1200px; overflow: hidden; background: var(--page); }
  body { font-family: "Open Sans", sans-serif; color: var(--text); position: relative; }
  .head-font { font-family: "Montserrat", sans-serif; }

  .flyer { position: absolute; top: 313px; width: 400px; height: 573px; overflow: hidden; background: var(--white); box-shadow: 0 2px 8px rgba(0,0,0,.12); }
  .flyer.front { left: 12px; }
  .flyer.back { left: 425px; }

  /* Header */
  .header { position: absolute; top: 0; left: 0; width: 100%; height: 72px; display: flex; align-items: center; justify-content: space-between; padding: 0 20px; }
  .brand { display: flex; align-items: center; gap: 7px; }
  .brand-mark { width: 22px; height: 22px; background: var(--navy); flex: none; }
  .brand-name { font-family: "Montserrat", sans-serif; font-weight: 800; color: var(--navy); font-size: 9px; line-height: 1.15; width: 92px; text-transform: uppercase; }
  .address { font-family: "Montserrat", sans-serif; font-weight: 700; color: var(--navy); font-size: 9px; line-height: 1.3; width: 190px; }

  /* Front hero */
  .hero { position: absolute; top: 72px; left: 0; width: 100%; height: 192px; }
  .hero-photo { position: absolute; left: 0; top: 0; width: 270px; height: 192px;
    background: linear-gradient(160deg, #8fb7d9 0%, #4f7fae 35%, #c4773a 70%, #2d4a6d 100%); }
  .hero-panel { position: absolute; right: 0; top: 0; width: 200px; height: 192px; background: var(--navy);
    clip-path: polygon(22% 0, 100% 0, 100% 100%, 0 100%); padding: 26px 14px 0 60px; }
  .hero-title { font-family: "Montserrat", sans-serif; font-weight: 900; font-size: 17px; line-height: 1.08; color: var(--white); text-transform: uppercase; }
  .hero-title .accent { color: var(--orange); display: block; }
  .hero-sub { margin-top: 9px; font-family: "Montserrat", sans-serif; font-weight: 700; font-size: 7.5px; line-height: 1.35; color: var(--orange); }
  .stripe { position: absolute; left: 0; width: 400px; height: 24px; }

  /* Front content */
  .content { position: absolute; top: 286px; left: 20px; right: 20px; display: flex; gap: 16px; }
  .welcome { width: 200px; }
  .welcome-kicker { font-family: "Montserrat", sans-serif; font-weight: 800; font-size: 12px; color: var(--navy); }
  .welcome-name { font-family: "Montserrat", sans-serif; font-weight: 800; font-size: 10.5px; color: var(--orange); text-transform: uppercase; margin-top: 1px; }
  .welcome-rule { width: 32px; height: 2px; background: var(--orange); margin: 6px 0 7px; }
  .welcome-text { font-size: 6.6px; line-height: 1.55; color: var(--text); }
  .welcome-photo { margin-top: 10px; width: 200px; height: 92px; background: linear-gradient(135deg, #d9dfe8, #a9b6c8 60%, #e6d6c1); }

  .calculator { flex: 1; }
  .calc-head { background: var(--orange); color: var(--white); font-family: "Montserrat", sans-serif; font-weight: 800; font-size: 8.5px; padding: 6px 8px; text-transform: uppercase; }
  .calc-body { background: var(--panel); padding: 8px; border: 1px solid #dfe3ec; border-top: none; }
  .calc-amount { font-family: "Montserrat", sans-serif; font-weight: 900; font-size: 18px; color: var(--navy); }
  .calc-note { font-size: 6.2px; line-height: 1.5; color: var(--muted); margin-top: 3px; }
  .calc-photo { margin-top: 8px; width: 100%; height: 104px; background: linear-gradient(160deg, #f1e4cf, #c99a63 55%, #8d6338); }

  /* Back hero */
  .back-hero { position: absolute; top: 72px; left: 0; width: 100%; height: 150px;
    background: linear-gradient(170deg, #9ec3df 0%, #6e8fb0 40%, #c98a45 75%, #3a4a62 100%); }

  /* Services */
  .services { position: absolute; top: 240px; left: 20px; right: 20px; }
  .section-title { font-family: "Montserrat", sans-serif; font-weight: 900; font-size: 13px; color: var(--navy); text-transform: uppercase; }
  .section-title span { color: var(--orange); }
  .section-rule { width: 32px; height: 2px; background: var(--orange); margin: 4px 0 8px; }
  .service-grid { display: grid; grid-template-columns: 1fr 1fr; gap: 0 16px; }
  .service-col { display: flex; flex-direction: column; gap: 7px; }
  .service { display: flex; gap: 6px; align-items: flex-start; }
  .service-icon { width: 16px; height: 16px; border-radius: 50%; background: var(--orange); flex: none; display: flex; align-items: center; justify-content: center; }
  .service-title { font-family: "Montserrat", sans-serif; font-weight: 800; font-size: 7.5px; color: var(--navy); text-transform: uppercase; }
  .service-text { font-size: 5.8px; line-height: 1.45; color: var(--muted); margin-top: 1px; }
  .service-photo { width: 100%; height: 42px; background: linear-gradient(160deg, #f1e4cf, #c99a63 55%, #8d6338); }

  /* News */
  .news { position: absolute; top: 405px; left: 20px; right: 20px; }
  .news-grid { display: grid; grid-template-columns: 1fr 1fr; gap: 12px; }
  .news-card { display: flex; gap: 6px; }
  .news-photo { width: 58px; height: 56px; flex: none; background: linear-gradient(140deg, #c9d3e0, #8ea3bd 60%, #d8c2a2); }
  .news-title { font-family: "Montserrat", sans-serif; font-weight: 800; font-size: 7px; color: var(--navy); line-height: 1.25; }
  .news-text { font-size: 5.8px; line-height: 1.45; color: var(--muted); margin-top: 3px; }

  /* Footer */
  .footer { position: absolute; bottom: 0; left: 0; width: 100%; height: 36px; background: var(--navy); display: flex; align-items: center; justify-content: space-between; padding: 0 20px; }
  .footer-item { display: flex; align-items: center; gap: 5px; color: var(--white); font-family: "Montserrat", sans-serif; font-weight: 700; font-size: 7.5px; }
  .footer-web { color: var(--orange); font-family: "Montserrat", sans-serif; font-weight: 700; font-size: 7.5px; }
</style>
</head>
<body>

<!-- Front side -->
<article class="flyer front">
  <header class="header">
    <div class="brand">
      <div class="brand-mark"></div>
      <div class="brand-name">Brom-leigh Sky Harbour</div>
    </div>
    <div class="address">Shop 8 Westbury Commercial Complex, 238-240 Halden Brook Road Kingston 8, Jamaica West Indies</div>
  </header>

  <section class="hero">
    <div class="hero-photo" role="img" aria-label="Cargo ship with stacked shipping containers at port, with a cargo plane overhead"></div>
    <div class="hero-panel">
      <h1 class="hero-title"><span class="accent">Shop Online</span>From the USA and Ship to Jamaica</h1>
      <p class="hero-sub">Customs Brokerage, Import Export and Logistic Services</p>
    </div>
    <svg class="stripe" style="top:178px" viewBox="0 0 400 24" aria-hidden="true">
      <polygon points="0,10 400,0 400,7 0,17" fill="var(--yellow)"/>
      <polygon points="0,17 400,7 400,24 0,24" fill="var(--white)"/>
    </svg>
  </section>

  <section class="content">
    <div class="welcome">
      <h2 class="welcome-kicker">WELCOME TO</h2>
      <div class="welcome-name">Brom-leigh Sky Harbour</div>
      <div class="welcome-rule"></div>
      <p class="welcome-text">We help families and businesses across Jamaica buy from US stores with ease. Send your online orders to our Miami address and we handle customs clearance, duties and delivery to your door. Fast, reliable and fully tracked service every week.</p>
      <div class="welcome-photo" role="img" aria-label="Hands typing on a laptop while shopping online"></div>
    </div>
    <div class="calculator">
      <div class="calc-head">Shipping Calculator</div>
      <div class="calc-body">
        <div class="calc-amount">$: 0 USD</div>
        <p class="calc-note">Estimate your shipping cost before you buy. Check our website for full rates.</p>
      </div>
      <div class="calc-photo" role="img" aria-label="Stack of cardboard shipping boxes"></div>
    </div>
  </section>

  <footer class="footer">
    <div class="footer-item">
      <svg width="10" height="10" viewBox="0 0 24 24" aria-hidden="true"><path fill="var(--orange)" d="M6.6 10.8a15.1 15.1 0 0 0 6.6 6.6l2.2-2.2a1 1 0 0 1 1-.25 11.4 11.4 0 0 0 3.6.57 1 1 0 0 1 1 1V20a1 1 0 0 1-1 1A17 17 0 0 1 3 4a1 1 0 0 1 1-1h3.5a1 1 0 0 1 1 1c0 1.25.2 2.45.57 3.57a1 1 0 0 1-.25 1z"/></svg>
      <span>(876) 555-0148 / (876) 555-0193</span>
    </div>
    <div class="footer-web">www.bromleighskyharbour.com</div>
  </footer>
</article>

<!-- Back side -->
<article class="flyer back">
  <header class="header">
    <div class="brand">
      <div class="brand-mark"></div>
      <div class="brand-name">Brom-leigh Sky Harbour</div>
    </div>
    <div class="address">Shop 8 Westbury Commercial Complex, 238-240 Halden Brook Road Kingston 8, Jamaica West Indies</div>
  </header>

  <section class="back-hero" role="img" aria-label="Freight trucks on a highway with a cargo plane and ship under a sunset sky"></section>
  <svg class="stripe" style="top:208px" viewBox="0 0 400 24" aria-hidden="true">
    <polygon points="0,10 400,0 400,7 0,17" fill="var(--yellow)"/>
    <polygon points="0,17 400,7 400,24 0,24" fill="var(--white)"/>
  </svg>

  <section class="services">
    <h2 class="section-title">Our <span>Services</span></h2>
    <div class="section-rule"></div>
    <div class="service-grid">
      <div class="service-col">
        <div class="service">
          <div class="service-icon"><svg width="9" height="9" viewBox="0 0 24 24" aria-hidden="true"><path fill="var(--white)" d="M3 7h11v9H3zM14 10h4l3 3v3h-7z"/><circle cx="7" cy="18" r="2" fill="var(--white)"/><circle cx="17" cy="18" r="2" fill="var(--white)"/></svg></div>
          <div><div class="service-title">Shipping</div><p class="service-text">Weekly air and sea freight from Miami to Kingston.</p></div>
        </div>
        <div class="service">
          <div class="service-icon"><svg width="9" height="9" viewBox="0 0 24 24" aria-hidden="true"><path fill="var(--white)" d="M3 7l9-4 9 4v10l-9 4-9-4z"/></svg></div>
          <div><div class="service-title">Logistics</div><p class="service-text">Storage, packing and island-wide delivery handled for you.</p></div>
        </div>
        <div class="service">
          <div class="service-icon"><svg width="9" height="9" viewBox="0 0 24 24" aria-hidden="true"><path fill="none" stroke="var(--white)" stroke-width="3" d="M4 12l5 5L20 6"/></svg></div>
          <div><div class="service-title">Custom Clearance</div><p class="service-text">Licensed brokers prepare entries and pay duties quickly.</p></div>
        </div>
      </div>
      <div class="service-col">
        <div class="service">
          <div class="service-icon"><svg width="9" height="9" viewBox="0 0 24 24" aria-hidden="true"><path fill="none" stroke="var(--white)" stroke-width="3" d="M12 3v14M6 11l6 6 6-6"/></svg></div>
          <div><div class="service-title">Imports</div><p class="service-text">Commercial and personal imports cleared with care.</p></div>
        </div>
        <div class="service">
          <div class="service-icon"><svg width="9" height="9" viewBox="0 0 24 24" aria-hidden="true"><path fill="var(--white)" d="M6.6 10.8a15.1 15.1 0 0 0 6.6 6.6l2.2-2.2a1 1 0 0 1 1-.25 11.4 11.4 0 0 0 3.6.57 1 1 0 0 1 1 1V20a1 1 0 0 1-1 1A17 17 0 0 1 3 4a1 1 0 0 1 1-1h3.5a1 1 0 0 1 1 1c0 1.25.2 2.45.57 3.57a1 1 0 0 1-.25 1z"/></svg></div>
          <div><div class="service-title">Support</div><p class="service-text">Friendly staff ready to track every package.</p></div>
        </div>
        <div class="service-photo" role="img" aria-label="Cardboard parcels ready for delivery"></div>
      </div>
    </div>
  </section>

  <section class="news">
    <h2 class="section-title">Latest <span>News</span></h2>
    <div class="section-rule"></div>
    <div class="news-grid">
      <div class="news-card">
        <div class="news-photo" role="img" aria-label="Shipping containers at a port"></div>
        <div><div class="news-title">New Weekly Sea Freight</div><p class="news-text">Extra sailings now leave Miami every Friday for Kingston.</p></div>
      </div>
      <div class="news-card">
        <div class="news-photo" role="img" aria-label="Cargo plane being loaded"></div>
        <div><div class="news-title">Faster Air Cargo Times</div><p class="news-text">Most air packages now arrive within three working days.</p></div>
      </div>
    </div>
  </section>

  <footer class="footer">
    <div class="footer-item">
      <svg width="10" height="10" viewBox="0 0 24 24" aria-hidden="true"><path fill="var(--orange)" d="M2 5h20v14H2z"/><path fill="none" stroke="var(--navy)" stroke-width="2" d="M2 5l10 8 10-8"/></svg>
      <span>info@bromleighskyharbour,com</span>
    </div>
    <div class="footer-web">www.bromleighskyharbour.com</div>
  </footer>
</article>

</body>
</html>
```